Digital Product Store Front for Educational Leaders (PraisewithPenelope)

I am an a Principal, Author and Education consultant I am in need of a wordpress website that fits my brand that I will be able to sell digital products I have created, digital courses I have created, and offer mentorship and coaching services. I have my branding documents and my content/wording in the files. This website should be professional yet relatable. I'd like it to be clean, easy to navigate and be very obvious with its purpose. Please view the attached documents to give a much clearer idea about my brand and wants. :)

Target Market(s)

Educational Leaders (Principals)

Industry/Entity Type

Educational Leadership

Coding

Coded - Design and coding required

Number of Pages Required

1 page

Font styles to use
Other font styles liked:
• please use my branding font

Requirements
Must have
• All the items I listed on my document, my brand colors and font, The content I submitted is still in a very draft format but just to give the designer and idea.

```html
<!DOCTYPE html>
<html lang="en">
<head>
<meta charset="utf-8">
<title>PraisewithPenelope</title>
<link rel="stylesheet" href="https://fonts.googleapis.com/css2?family=Josefin+Sans:wght@300;400;600&family=Arimo:wght@400&display=swap">
<style>
:root{
  --teal:#5a9e92;
  --cream:#f4efe4;
  --ink:#2a2a2a;
  --white:#ffffff;
  --photo-warm:#e9e1d8;
}
*{margin:0;padding:0;box-sizing:border-box}
html,body{width:1200px;height:4637px;overflow:hidden}
body{position:relative;background:var(--cream);font-family:"Josefin Sans",sans-serif;color:var(--ink);font-weight:300}
.abs{position:absolute}
.photo{position:absolute}
.btn{position:absolute;background:var(--teal);color:var(--white);font-size:22px;font-weight:300;display:flex;align-items:center;justify-content:center;letter-spacing:.5px}
.hero{position:absolute;left:0;top:0;width:1200px;height:720px;background:linear-gradient(180deg,#f1efec 0%,#ece6df 60%,var(--cream) 100%)}
.hero-photo{left:0;top:0;width:1200px;height:720px;background:radial-gradient(ellipse at 30% 45%,#d9c7b6 0%,#ebe3da 35%,rgba(240,236,231,0) 70%),radial-gradient(ellipse at 66% 40%,#e8c6b4 0%,rgba(232,198,180,0) 40%)}
.brand{left:32px;top:40px;width:204px;height:38px;display:flex;align-items:center;gap:8px;font-size:19px;font-weight:400;color:var(--teal);background:var(--white);padding:0 10px}
.brand-dot{width:10px;height:10px;background:var(--teal);border-radius:50%}
.nav{position:absolute;top:30px;left:646px;display:flex;font-family:Arimo,sans-serif;font-size:14px;color:var(--ink)}
.nav a{position:absolute;top:0;height:30px;line-height:30px;color:inherit;text-decoration:none;white-space:nowrap}
.nav a.active{background:var(--teal);color:var(--white);padding:0 9px}
.hero-title{left:637px;top:110px;font-size:38px;line-height:48px;font-weight:300;letter-spacing:1px}
.hero-text{left:639px;top:224px;width:400px;font-size:15px;line-height:23px}
.feature-title{font-size:38px;font-weight:300;letter-spacing:.5px}
.rule{height:2px;width:140px;background:var(--ink)}
.feature-text{font-size:19px;line-height:32px;width:440px}
.book-frame{left:133px;top:2207px;width:790px;height:551px;border:4px solid var(--teal)}
.book-frame::before{content:"";position:absolute;inset:8px;border:2px solid var(--teal)}
.book-text{left:205px;top:2272px;width:490px;font-size:27px;line-height:40px;font-weight:300}
.newsletter{left:0;top:2830px;width:1200px;height:322px;background:var(--teal);color:var(--white);text-align:center}
.news-title{position:absolute;left:0;width:1200px;top:68px;font-size:37px;letter-spacing:1.5px}
.news-sub{position:absolute;left:0;width:1200px;top:127px;font-size:28px}
.signup{position:absolute;left:218px;top:196px;width:765px;height:59px;background:var(--white);display:flex;align-items:center}
.signup .field{flex:1;display:flex;align-items:center;gap:14px;padding-left:24px;font-size:15px;color:var(--teal)}
.signup .go{width:106px;height:43px;margin-right:8px;background:var(--teal);color:var(--white);font-size:18px;display:flex;align-items:center;justify-content:center}
.meet-title{left:130px;top:3217px;font-size:40px}
.meet-text{left:133px;width:470px;font-size:18.5px;line-height:32px;text-align:justify}
.message{left:133px;top:3834px;width:936px;height:355px;border:4px solid var(--teal);padding:40px 36px 0}
.message h3{font-size:31px;font-weight:300;color:var(--teal);margin-bottom:18px}
.message p{font-size:14.5px;line-height:27px;margin-bottom:12px}
.footer{left:0;top:4271px;width:1200px;height:366px;background:var(--teal);color:var(--white)}
.footer-brand{position:absolute;left:349px;top:80px;width:504px;height:48px;background:var(--white);color:var(--teal);display:flex;align-items:center;justify-content:center;gap:12px;font-size:26px;font-weight:400}
.footer-brand .sq{width:14px;height:14px;background:var(--teal)}
.footer-nav{position:absolute;top:256px;left:0;width:1200px;font-family:Arimo,sans-serif;font-size:14px}
.footer-nav span{position:absolute;white-space:nowrap}
.copy{position:absolute;top:308px;left:0;width:1200px;text-align:center;font-family:Arimo,sans-serif;font-size:13px}
</style>
</head>
<body>

<section class="hero">
  <div class="photo hero-photo" role="img" aria-label="Smiling woman at a desk with a blush laptop, glasses and a white vase"></div>
  <div class="abs brand"><span class="brand-dot"></span>PraisewithPenelope</div>
  <nav class="nav">
    <a class="active" style="left:0">HOME</a>
    <a style="left:88px">SHOP</a>
    <a style="left:163px">LEARN</a>
    <a style="left:249px">PARTNER</a>
    <a style="left:358px">BOOK</a>
    <a style="left:442px">MEET ME</a>
  </nav>
  <h1 class="abs hero-title" style="font-weight:300">YOUR SCHOOL CAN<br>ABSOLUTELY THRIVE.</h1>
  <p class="abs hero-text">Let's partner together to revolutionize your school's culture Into an engaged, high-performing community where everyone belongs. (Why wait?)</p>
</section>

<div class="photo" style="left:133px;top:769px;width:436px;height:416px;background:linear-gradient(135deg,#3d3a36,#7a6a58 55%,#c9a676)" role="img" aria-label="Hands on a laptop with floating digital file icons"></div>
<h2 class="abs feature-title" style="left:626px;top:820px">DIGITAL TOOLS</h2>
<div class="abs rule" style="left:628px;top:887px"></div>
<p class="abs feature-text" style="left:629px;top:922px">From staff and student events, to these digital tools are just one File. Print. away from revolutionalizing your school culture. (Printed in color of course) (Get that color ink ready!)</p>
<div class="btn" style="left:632px;top:1087px;width:108px;height:47px">SHOP</div>

<h2 class="abs feature-title" style="left:133px;top:1265px">INNOVATICE COURSES</h2>
<div class="abs rule" style="left:135px;top:1332px"></div>
<p class="abs feature-text" style="left:134px;top:1367px;width:390px">Join an individual or team online training course designed to elevate your leadership skills, revolutionize your school culture or transform student behvaior. (And you can even say you thought of it yourself) IDK something at the end</p>
<div class="btn" style="left:137px;top:1584px;width:119px;height:47px">LEARN</div>
<div class="photo" style="left:632px;top:1247px;width:436px;height:416px;background:linear-gradient(135deg,#d8dcdc,#a9b3b4 50%,#2f4b55)" role="img" aria-label="Young man with headphones taking notes at a laptop"></div>

<div class="photo" style="left:133px;top:1724px;width:436px;height:416px;background:linear-gradient(180deg,#12223a 0%,#1b2f4a 62%,#8a5a32 80%,#5e3a20 100%)" role="img" aria-label="Wooden figure climbing block steps labeled leadership"></div>
<h2 class="abs feature-title" style="left:628px;top:1776px">AUTHENTIC COACHING</h2>
<div class="abs rule" style="left:630px;top:1843px"></div>
<p class="abs feature-text" style="left:630px;top:1878px;width:390px">Unleash your leadership potential in this mentorship experience as we work together to curate a personalized plan to (Let's Be Smart Friends!)</p>
<div class="btn" style="left:632px;top:2043px;width:142px;height:47px">PARTNER</div>

<div class="abs book-frame"></div>
<p class="abs book-text">The most important tool to connect your community and create a high-performing, thriving culture is YOU! Start by unleashing a people-centered leadership style and learn all the #1 Rules to create the culture you dream about by reading an Riverbook #1 New Release Start With Culture.</p>
<div class="btn" style="left:207px;top:2624px;width:151px;height:49px">BUY NOW</div>
<div class="photo" style="left:733px;top:2234px;width:331px;height:495px;background:linear-gradient(180deg,#f3efe9,#e3d6c8 55%,#f1ebe3)" role="img" aria-label="Book cover of Start With Culture by Penelope Hartwell, author photo in cream sweater"></div>

<section class="abs newsletter">
  <h2 class="news-title" style="font-weight:300">SIGN-UP FOR THE PRAISEWITHPENELOPE NEWSLETTER</h2>
  <p class="news-sub">(Who doesn't want more emails?)</p>
  <div class="signup">
    <div class="field">
      <svg width="18" height="14" viewBox="0 0 18 14" fill="none" stroke="#5a9e92" stroke-width="1.4"><rect x="1" y="1" width="16" height="12"/><path d="M1 1l8 7 8-7"/></svg>
      Email id
    </div>
    <div class="go">SIGNUP</div>
  </div>
</section>

<h2 class="abs meet-title" style="font-weight:300">MEET ME</h2>
<p class="abs meet-text" style="top:3318px">Welcome to PraisewithPenelope! I am Penelope Hartwell an Elementary Principal in Fairhaven, Ohio, Author of Start With Culture, and Education Consultant. I am super passionate about bringing change to the way school leaders serve –both children and adults.</p>
<p class="abs meet-text" style="top:3510px">I was a teacher for eight years, and then an instructional coach, before earning my dream job as an elementary school principal! I am now in my sixth year as a school leader and have dramatically shifted the traditional elementary school culture into a thriving, loving community.</p>
<div class="btn" style="left:133px;top:3728px;width:187px;height:47px">CONTACT ME</div>
<div class="photo" style="left:612px;top:3294px;width:540px;height:450px;background:radial-gradient(ellipse at 45% 45%,#d7c6b6 0%,#ebe1d6 40%,rgba(244,239,228,0) 72%)" role="img" aria-label="Smiling woman resting her head on her hand beside a laptop"></div>

<section class="abs message">
  <h3>A Message from Me</h3>
  <p>I am so happy you are here! (Seriously!) Working with other educational leaders brings me THE. MOST. JOY. (I'm OBSESSED)</p>
  <p>I want to support you on every inch of your journey! We can work alongside each other to navigate the challenges of leading adults, transforming student behaviors, and creating a vibrant atmosphere.</p>
  <p>School leadership can be lonely, taxing, and overwhelming. Often, the biggest challenge is knowing where to start as you face the pressures and demands from the many stakeholders. But don't worry, I can't wait to help you!</p>
  <p>So whether you need tools to enhance your own leadership skills, to facilitate connection within your community, or to transform student behaviors, I am here to help you develop your school into a high-performing culture. Let's get started today!!</p>
</section>

<footer class="abs footer">
  <div class="footer-brand"><span class="sq"></span>PraisewithPenelope</div>
  <div class="footer-nav">
    <span style="left:351px">HOME</span>
    <span style="left:428px">SHOP</span>
    <span style="left:503px">LEARN</span>
    <span style="left:591px">PARTNER</span>
    <span style="left:700px">BOOK</span>
    <span style="left:784px">MEET ME</span>
  </div>
  <p class="copy">Copyright © 2024 All Rights Reserved</p>
</footer>

</body>
</html>
```